Tallowfern Studio business cards

We are a new company based in New Zealand. We Specialize in High end Luxury Residential Architecture.

Every home is bespoke and is designed to each clients individual requirements and needs.

I like to design buildings that inspire people through light and form while offering a high level of comfort and usability.

Lines of sight, proportion and balance are fundamental to the spaces I create.
Updates

August 5th is current deadline - Today's date is the 13th of August.

Target Market(s)

New Zealanders who want a custom individual home design, typically 30-65 year old males and females

Industry/Entity Type

Architecture

Contact Information for Business Card

Director - Derek Holloway
Contact Number - 0274619037
Email - info@tallowfernstudio.co.nz
Webstie - www.tallowfernstudio.co.nz
Social Media - @tallowfernstudio

Font styles to use
Sans Serif

Requirements
Must have
• Logo (Both Sides)
Website
Email
Contact Number
Social Media

Nice to have
• Texture
Should not have
• More than 3 colours - typically I would've thought 2 would be good to match the logo.

```html
<!DOCTYPE html>
<html lang="en">
<head>
<meta charset="utf-8">
<title>Tallowfern Studio — Business Cards</title>
<link rel="stylesheet" href="https://fonts.googleapis.com/css2?family=Jost:wght@300;400&display=swap">
<style>
  :root {
    --backdrop: #b3b4b6;
    --card-light: #ebebea;
    --card-dark: #5f5f62;
    --ink: #2b2b2d;
    --ink-soft: #6a6a6c;
    --ink-light: #f4f4f4;
  }
  html, body {
    margin: 0;
    padding: 0;
    width: 1200px;
    height: 966px;
    overflow: hidden;
    background: var(--backdrop);
    font-family: "Jost", sans-serif;
  }
  .sheet {
    width: 1200px;
    height: 966px;
    display: flex;
    align-items: center;
    justify-content: center;
    gap: 70px;
  }
  .card {
    width: 440px;
    height: 720px;
    box-sizing: border-box;
    position: relative;
    overflow: hidden;
    box-shadow: 0 14px 30px rgba(0,0,0,0.18);
  }
  .card--front { background: var(--card-light); color: var(--ink); }
  .card--back { background: var(--card-dark); color: var(--ink-light); }

  .brand {
    position: absolute;
    left: 0;
    right: 0;
    display: flex;
    flex-direction: column;
    align-items: center;
  }
  .card--front .brand { top: 120px; }
  .card--back .brand { top: 250px; }
  .brand__dot {
    width: 40px;
    height: 40px;
    border: 3px solid currentColor;
    border-radius: 50%;
    margin-bottom: 22px;
  }
  .brand__name {
    font-weight: 400;
    font-size: 30px;
    letter-spacing: 0.45em;
    margin: 0 0 0 0.45em;
    line-height: 1;
  }
  .brand__sub {
    font-weight: 300;
    font-size: 12px;
    letter-spacing: 3.4em;
    margin: 12px 0 0 3.4em;
    line-height: 1;
  }

  .person {
    position: absolute;
    top: 330px;
    left: 0;
    right: 0;
    text-align: center;
  }
  .person__name {
    font-weight: 400;
    font-size: 23px;
    letter-spacing: 0.06em;
    text-transform: uppercase;
    margin: 0;
  }
  .person__role {
    font-weight: 300;
    font-size: 18px;
    letter-spacing: 0.04em;
    color: var(--ink-soft);
    margin: 2px 0 0;
  }

  .contact {
    position: absolute;
    top: 510px;
    left: 0;
    right: 0;
    text-align: center;
    font-weight: 300;
    font-size: 18px;
    letter-spacing: 0.07em;
    line-height: 1.55;
    color: var(--ink-soft);
  }
  .contact p { margin: 0; }
  .contact__phone { margin-bottom: 26px !important; letter-spacing: 0.12em; }
</style>
</head>
<body>
  <main class="sheet">
    <section class="card card--front" aria-label="Business card front">
      <div class="brand">
        <span class="brand__dot" aria-hidden="true"></span>
        <p class="brand__name">TALLOWFERN</p>
        <p class="brand__sub">STUDIO</p>
      </div>
      <div class="person">
        <p class="person__name">Derek Holloway</p>
        <p class="person__role">Director</p>
      </div>
      <div class="contact">
        <p class="contact__phone">0274619037</p>
        <p>info@tallowfernstudio.co.nz</p>
        <p>www.tallowfernstudio.co.nz</p>
        <p>@tallowfernstudio</p>
      </div>
    </section>

    <section class="card card--back" aria-label="Business card back">
      <div class="brand">
        <span class="brand__dot" aria-hidden="true"></span>
        <p class="brand__name">TALLOWFERN</p>
        <p class="brand__sub">STUDIO</p>
      </div>
    </section>
  </main>
</body>
</html>
```